Stationery and Business Card Design

We need stationary design for our new company pelvanta. Pelvanta is a company that provides city apartment rentals for tourists in Athens We need business cards, letterheads for A4 and A5 and envelopes for A4 A5. The design needs to be modern, friendly and corporate.

Target Market(s)

City Tourists

Industry/Entity Type

Tourism

```html
<!DOCTYPE html>
<html lang="en">
<head>
<meta charset="utf-8">
<title>Pelvanta Apartments Stationery</title>
<link href="https://fonts.googleapis.com/css2?family=Raleway:wght@400;600&family=Roboto:wght@400;700&display=swap" rel="stylesheet">
<style>
:root{
  --bg:#e9e9ea;
  --paper:#f7f7f7;
  --plum:#7d1850;
  --charcoal:#3b3a3a;
  --ink:#555;
  --muted:#8a8a8a;
}
*{margin:0;padding:0;box-sizing:border-box}
html,body{width:1200px;height:758px;overflow:hidden;background:var(--bg)}
body{position:relative;font-family:"Roboto",Arial,sans-serif;color:var(--ink)}
.sheet{position:absolute;background:var(--paper);box-shadow:0 2px 6px rgba(0,0,0,.12);overflow:hidden}
.brand{position:absolute;display:flex;flex-direction:column;align-items:center;text-align:center}
.brand-square{background:var(--plum)}
.brand-name{font-family:"Raleway",sans-serif;font-weight:400;color:var(--plum);line-height:1}
.brand-sub{font-family:"Raleway",sans-serif;color:var(--plum);letter-spacing:.3em;display:flex;align-items:center;gap:4px;line-height:1}
.brand-sub::before,.brand-sub::after{content:"";display:block;width:14px;height:1px;background:currentColor;opacity:.6}
.footer-band{position:absolute;left:0;bottom:0;width:100%}
.flap{position:absolute;left:0;top:0;width:100%}
.flap-url{position:absolute;left:0;width:100%;text-align:center;color:#fff;font-size:5px;letter-spacing:.15em;transform:rotate(180deg)}

.card-front{left:84px;top:99px;width:144px;height:87px;background:var(--plum)}
.card-front .brand{left:0;right:0;top:24px}
.card-front .brand-square{width:18px;height:18px;background:#fff}
.card-front .brand-name{color:#fff;font-size:15px;margin-top:4px}
.card-front .brand-sub{color:#fff;font-size:3.5px;margin-top:2px}

.card-back{left:271px;top:99px;width:146px;height:87px}
.card-back .mark{position:absolute;left:18px;top:25px;width:36px;height:36px;background:var(--plum)}
.card-back .person{position:absolute;left:71px;top:24px}
.person-name{font-size:5.5px;font-weight:700;color:var(--plum)}
.person-title{font-size:3.5px;color:var(--muted);margin-bottom:5px}
.contact-line{font-size:3.3px;color:var(--ink);display:flex;align-items:center;gap:3px;line-height:6px;white-space:nowrap}
.dot{width:3px;height:3px;border-radius:50%;background:var(--plum);display:inline-block}

.letterhead{left:84px;top:226px;width:333px;height:471px}
.letterhead .brand{left:30px;top:28px;width:106px}
.letterhead .brand-square{width:28px;height:28px}
.letterhead .brand-name{font-size:20px;margin-top:5px}
.letterhead .brand-sub{font-size:4.5px;margin-top:3px}
.lh-contact{position:absolute;left:223px;top:26px}
.lh-company{font-size:6.5px;font-weight:700;color:var(--plum);margin-bottom:4px}
.lh-address{font-size:3.6px;line-height:5.5px;color:var(--ink);margin-top:2px}
.lh-body{position:absolute;left:36px;top:113px;width:261px;font-size:4.3px;line-height:7.5px;color:#6a6a6a;text-align:justify}
.lh-body p{margin-bottom:5px}
.lh-body .greeting{margin-bottom:12px}
.lh-sign{position:absolute;left:36px;top:353px;font-size:4.6px;line-height:7px;color:#6a6a6a}
.signature{width:40px;height:12px;margin:1px 0;background:linear-gradient(90deg,rgba(50,80,160,.25),rgba(50,80,160,.1))}

.a5{left:484px;top:62px;width:235px;height:333px}
.a5 .brand{left:20px;top:22px;width:68px}
.a5 .brand-square{width:15px;height:15px}
.a5 .brand-name{font-size:12px;margin-top:3px}
.a5 .brand-sub{font-size:3px;margin-top:2px}

.env-small{left:433px;top:411px;width:333px;height:286px}
.env-small .brand{left:16px;top:75px;width:68px}
.env-small .brand-square{width:16px;height:16px}
.env-small .brand-name{font-size:13px;margin-top:3px}
.env-small .brand-sub{font-size:3.2px;margin-top:2px}
.env-large{left:783px;top:176px;width:333px;height:521px}
.env-large .brand{left:20px;top:72px;width:68px}
.env-large .brand-square{width:16px;height:16px}
.env-large .brand-name{font-size:13px;margin-top:3px}
.env-large .brand-sub{font-size:3.2px;margin-top:2px}
</style>
</head>
<body>

<section class="sheet card-front" aria-label="Business card front">
  <div class="brand">
    <div class="brand-square"></div>
    <div class="brand-name">Pelvanta</div>
    <div class="brand-sub">APARTMENTS</div>
  </div>
</section>

<section class="sheet card-back" aria-label="Business card back">
  <div class="mark"></div>
  <div class="person">
    <div class="person-name">Mara Doukas</div>
    <div class="person-title">Your Title</div>
    <div class="contact-line"><span class="dot"></span>+00 111 222 3333</div>
    <div class="contact-line"><span class="dot"></span>stay@pelvanta-stays.gr</div>
    <div class="contact-line"><span class="dot"></span>www.pelvanta-stays.gr</div>
    <div class="contact-line">Your Long Commercial or</div>
    <div class="contact-line">business address in 2 line</div>
  </div>
</section>

<section class="sheet letterhead" aria-label="A4 letterhead">
  <div class="brand">
    <div class="brand-square"></div>
    <div class="brand-name">Pelvanta</div>
    <div class="brand-sub">APARTMENTS</div>
  </div>
  <div class="lh-contact">
    <div class="lh-company">Pelvanta Apartments</div>
    <div class="contact-line"><span class="dot"></span>+00 111 222 3333</div>
    <div class="contact-line"><span class="dot"></span>stay@pelvanta-stays.gr</div>
    <div class="contact-line"><span class="dot"></span>www.pelvanta-stays.gr</div>
    <div class="lh-address">Your Long Commercial or business<br>address in 2 line</div>
  </div>
  <div class="lh-body">
    <p class="greeting">Dear Sir,</p>
    <p>Lorem Ipsum is simply dummy text of the printing and typesetting industry. Lorem Ipsum has been the industry's standard dummy text ever since the 1500s, when an unknown printer took a galley of type and scrambled it to make a type specimen book. It has survived not only five centuries, but also the leap into electronic typesetting, remaining essentially unchanged. It was popularised in the 1960s with the release of transfer sheets containing Lorem Ipsum passages, and more recently with desktop publishing software and layout tools including versions of Lorem Ipsum.</p>
    <p>Lorem Ipsum is simply dummy text of the printing and typesetting industry. Lorem Ipsum has been the industry's standard dummy text ever since the 1500s, when an unknown printer took a galley of type and scrambled it to make a type specimen book. It has survived not only five centuries, but also the leap into electronic typesetting, remaining essentially unchanged. It was popularised in the 1960s with the release of transfer sheets containing Lorem Ipsum passages, and more recently with desktop publishing software and layout tools including versions of Lorem Ipsum.</p>
    <p>Lorem Ipsum is simply dummy text of the printing and typesetting industry. Lorem Ipsum has been the industry's standard dummy text ever since the 1500s, when an unknown printer took a galley of type and scrambled it to make a type specimen book.</p>
    <p>Lorem Ipsum is simply dummy text of the printing and typesetting industry. Lorem Ipsum has been the industry's standard dummy text ever since the 1500s, when an unknown printer took a galley of type and scrambled it to make a type specimen book. It has survived not only five centuries, but also the leap into electronic typesetting, remaining essentially unchanged. It was popularised in the 1960s with the release of transfer sheets containing Lorem Ipsum passages, and more recently with desktop publishing software and layout tools including versions of Lorem Ipsum.</p>
    <p>Lorem Ipsum has been the industry's standard dummy text ever since the 1500s, when an unknown printer took a galley of type and scrambled it to make a type specimen book.</p>
  </div>
  <div class="lh-sign">
    <div>Your Name</div>
    <div class="signature" role="img" aria-label="Handwritten signature"></div>
    <div>CEO | Owner</div>
  </div>
  <svg class="footer-band" width="333" height="8" viewBox="0 0 333 8" aria-hidden="true">
    <rect x="0" y="2" width="333" height="6" fill="var(--plum)"/>
    <polygon points="220,8 232,2 333,2 333,8" fill="var(--charcoal)"/>
  </svg>
</section>

<section class="sheet a5" aria-label="A5 letterhead">
  <div class="brand">
    <div class="brand-square"></div>
    <div class="brand-name">Pelvanta</div>
    <div class="brand-sub">APARTMENTS</div>
  </div>
  <svg class="footer-band" width="235" height="8" viewBox="0 0 235 8" aria-hidden="true">
    <rect x="0" y="2" width="235" height="6" fill="var(--plum)"/>
    <polygon points="155,8 166,2 235,2 235,8" fill="var(--charcoal)"/>
  </svg>
</section>

<section class="sheet env-small" aria-label="A5 envelope">
  <svg class="flap" width="333" height="52" viewBox="0 0 333 52" aria-hidden="true">
    <path d="M0 52 L0 20 Q0 2 18 2 L312 2 Q333 2 333 20 L333 52 Z" fill="var(--plum)"/>
  </svg>
  <div class="flap-url" style="top:16px">www.pelvanta-stays.gr</div>
  <div class="brand">
    <div class="brand-square"></div>
    <div class="brand-name">Pelvanta</div>
    <div class="brand-sub">APARTMENTS</div>
  </div>
  <svg class="footer-band" style="bottom:24px" width="333" height="4" viewBox="0 0 333 4" aria-hidden="true">
    <rect x="0" y="0" width="333" height="4" fill="var(--plum)"/>
    <polygon points="228,4 236,0 333,0 333,4" fill="var(--charcoal)"/>
  </svg>
</section>

<section class="sheet env-large" aria-label="A4 envelope">
  <svg class="flap" width="333" height="50" viewBox="0 0 333 50" aria-hidden="true">
    <path d="M0 50 L0 20 Q0 2 18 2 L312 2 Q333 2 333 20 L333 50 Z" fill="var(--plum)"/>
  </svg>
  <div class="flap-url" style="top:20px">www.pelvanta-stays.gr</div>
  <div class="brand">
    <div class="brand-square"></div>
    <div class="brand-name">Pelvanta</div>
    <div class="brand-sub">APARTMENTS</div>
  </div>
  <svg class="footer-band" style="bottom:24px" width="333" height="4" viewBox="0 0 333 4" aria-hidden="true">
    <rect x="0" y="0" width="333" height="4" fill="var(--plum)"/>
    <polygon points="228,4 236,0 333,0 333,4" fill="var(--charcoal)"/>
  </svg>
</section>

</body>
</html>
```